BEACON traffic management plans

The preparation of traffic management plans for architects, builders, landscapers for council approval. The preparation of the plans can include submitting to council, briefing the builder regarding management of the plan, onsite visit, taking photographs, measurements and establishing the best outcome. Implementing the plan can also take place if need be.
NO EXISTING LOGO AVAILABLE
No photos or documents available to upload

Target Market(s)

Builders, architects, landscapers
No existing logo availalble

Industry/Entity Type

Builders

Contact Information for Business Card

BEACON Traffic Management Plans
Tom Ridgway
harbourlane@westnetmail.com.au
0427 615 938

Font styles to use
Serif

Colors
1b1b1b

Requirements
Must have
• competitive prices
• No existing logo available
• No photos available
Nice to have
• Black with orange and white
• No existing logo available no
Should not have
• no existing logo available
• No photos or documents to upload

```html
<!DOCTYPE html>
<html lang="en">
<head>
<meta charset="utf-8">
<title>BEACON Traffic Management Plans – Business Card</title>
<link rel="stylesheet" href="https://fonts.googleapis.com/css2?family=Tinos:wght@400;700&display=swap">
<style>
  :root {
    --page-bg: #d9d4cc;
    --card-black: #1b1b1b;
    --card-black-deep: #0d0d0d;
    --accent-orange: #e8643a;
    --text-white: #f2f2f2;
    --rule-white: #e6e6e6;
  }
  html, body {
    margin: 0;
    padding: 0;
    width: 1200px;
    height: 1022px;
    overflow: hidden;
    background: var(--page-bg);
  }
  .stage {
    position: relative;
    width: 1200px;
    height: 1022px;
  }
  .business-card {
    position: absolute;
    left: 100px;
    top: 225px;
    width: 1000px;
    height: 571px;
    border-radius: 26px;
    background: linear-gradient(135deg, #2a2a2a 0%, var(--card-black) 40%, var(--card-black-deep) 100%);
    box-shadow: 0 18px 40px rgba(0, 0, 0, 0.35);
    overflow: hidden;
    font-family: "Tinos", "Times New Roman", serif;
  }
  .brand {
    position: absolute;
    left: 62px;
    top: 150px;
  }
  .brand-name {
    margin: 0;
    font-size: 136px;
    font-weight: 400;
    line-height: 1;
    letter-spacing: 2px;
    color: var(--accent-orange);
  }
  .brand-tagline {
    margin: 4px 0 0 36px;
    font-size: 44px;
    font-weight: 400;
    line-height: 1;
    color: var(--text-white);
  }
  .contact {
    position: absolute;
    left: 446px;
    right: 0;
    top: 404px;
  }
  .contact-name-row {
    display: flex;
    align-items: flex-end;
  }
  .contact-name {
    margin: 0;
    font-size: 38px;
    font-weight: 700;
    letter-spacing: 1px;
    line-height: 1;
    color: var(--accent-orange);
    white-space: nowrap;
  }
  .name-rule {
    flex: 1;
    height: 2px;
    margin: 0 0 6px 10px;
    background: var(--rule-white);
  }
  .contact-line {
    display: flex;
    align-items: center;
    margin-top: 12px;
    font-size: 29px;
    line-height: 1;
    color: var(--text-white);
  }
  .contact-line svg {
    width: 20px;
    height: 20px;
    margin-right: 16px;
    flex: none;
  }
</style>
</head>
<body>
<main class="stage">
  <section class="business-card">
    <div class="brand">
      <h1 class="brand-name">BEACON</h1>
      <p class="brand-tagline">Traffic Management Plans</p>
    </div>

    <div class="contact">
      <div class="contact-name-row">
        <p class="contact-name">TOM RIDGWAY</p>
        <div class="name-rule"></div>
      </div>
      <div class="contact-line">
        <svg viewBox="0 0 20 20" aria-hidden="true">
          <path d="M5 2 L8 2 L9 6 L7 8 Q9 12 12 13 L14 11 L18 12 L18 15 Q17 18 14 18 Q4 16 2 6 Q2 3 5 2 Z" fill="none" stroke="var(--accent-orange)" stroke-width="2"/>
        </svg>
        <span>0427 615 938</span>
      </div>
      <div class="contact-line">
        <svg viewBox="0 0 20 20" aria-hidden="true">
          <rect x="2" y="4" width="16" height="12" fill="none" stroke="var(--accent-orange)" stroke-width="2"/>
          <path d="M2 4 L10 11 L18 4" fill="none" stroke="var(--accent-orange)" stroke-width="2"/>
        </svg>
        <span>harbourlane@quaylinemail.com.au</span>
      </div>
    </div>
  </section>
</main>
</body>
</html>
```